Business Card Design Project

Recently had a new logo made up for my company and new business cards done as well. I have attached the logos for your viewing. Additional projects may be needed. Good luck!

Industry/Entity Type

Business

```html
<!DOCTYPE html>
<html lang="en">
<head>
<meta charset="utf-8">
<title>Harrow Financial Group — Business Cards</title>
<link href="https://fonts.googleapis.com/css2?family=Cinzel:wght@400;600&display=swap" rel="stylesheet">
<style>
  :root {
    --backdrop: #2a2a2c;
    --card-navy: #23232d;
    --band-gold: #d3c08e;
    --ink-gold: #c9ae72;
    --ink-dark: #2a2a30;
    --rule: #5b5a5e;
  }
  * { margin: 0; padding: 0; box-sizing: border-box; }
  html, body { width: 1200px; height: 1000px; overflow: hidden; }
  body {
    background: var(--backdrop);
    font-family: "Cinzel", "Times New Roman", serif;
    position: relative;
  }
  .card {
    position: absolute;
    width: 523px;
    height: 297px;
    background: var(--card-navy);
    overflow: hidden;
  }
  .card--front { left: 221px; top: 176px; }
  .card--back  { left: 507px; top: 547px; }

  /* Front */
  .front-brand {
    position: absolute;
    left: 0; right: 0; top: 46px;
    display: flex; flex-direction: column; align-items: center;
  }
  .brand-square {
    width: 110px; height: 118px;
    border: 6px solid var(--ink-gold);
  }
  .front-brand .brand-name {
    margin-top: 16px;
    color: var(--ink-gold);
    font-weight: 600;
    font-size: 22px;
    letter-spacing: 2px;
    text-align: center;
    line-height: 1.15;
    text-transform: uppercase;
  }
  .front-band {
    position: absolute;
    left: 0; right: 0; bottom: 0; height: 35px;
    background: var(--band-gold);
    border-top: 2px solid var(--rule);
    display: flex; flex-direction: column; align-items: center; justify-content: center;
    color: var(--ink-dark);
    font-size: 7.5px;
    letter-spacing: 1.6px;
    text-transform: uppercase;
  }
  .front-band .holder-name {
    padding: 0 14px 1px;
    border-bottom: 1px solid rgba(42,42,48,0.45);
  }
  .front-band .web { padding-top: 1px; }

  /* Back */
  .back-details {
    position: absolute;
    left: 0; right: 0; top: 36px;
    text-align: center;
    color: var(--ink-gold);
    text-transform: uppercase;
  }
  .back-details .holder-name { font-size: 15px; letter-spacing: 4px; }
  .back-details .holder-role { font-size: 9px; letter-spacing: 2.6px; margin-top: 2px; }
  .back-details .contact {
    margin-top: 14px;
    font-size: 7.5px; letter-spacing: 1.8px; line-height: 10px;
  }
  .back-details .address {
    margin-top: 9px;
    font-size: 7.5px; letter-spacing: 1.8px; line-height: 10px;
  }
  .back-band {
    position: absolute;
    left: 0; right: 0; bottom: 0; height: 121px;
    background: var(--band-gold);
    border-top: 2px solid var(--rule);
    display: flex; flex-direction: column; align-items: center;
    padding-top: 14px;
  }
  .back-band .brand-square {
    width: 74px; height: 78px;
    border: 5px solid var(--ink-dark);
  }
  .back-band .brand-name {
    margin-top: 4px;
    padding: 2px 8px 0;
    border-top: 1px solid rgba(42,42,48,0.45);
    color: var(--ink-dark);
    font-size: 8px;
    letter-spacing: 1.5px;
    text-transform: uppercase;
  }
</style>
</head>
<body>
  <section class="card card--front" aria-label="Business card front">
    <div class="front-brand">
      <div class="brand-square"></div>
      <div class="brand-name">Harrow<br>Financial Group</div>
    </div>
    <div class="front-band">
      <div class="holder-name">Daniel R. Harrow</div>
      <div class="web">www.harrowfinancial.com</div>
    </div>
  </section>

  <section class="card card--back" aria-label="Business card back">
    <div class="back-details">
      <div class="holder-name">Daniel R. Harrow</div>
      <div class="holder-role">Estate Planning and Insurance Specialist</div>
      <div class="contact">
        dharrow@harrowfinancial.com<br>
        P: 555-210-4837 | F: 555-210-4890<br>
        www.harrowfinancial.com
      </div>
      <div class="address">
        1450 Meadow Ridge Road, Suite 310E<br>
        Fairhaven, New York 10990
      </div>
    </div>
    <div class="back-band">
      <div class="brand-square"></div>
      <div class="brand-name">Harrow Financial Group</div>
    </div>
  </section>
</body>
</html>
```